Business card design needed

Family General Practitioner/ Family Physician.
Logo is the logo of the Crestmoor Guild of Family Clinicians Australia
http://kvplm.tarevo.edu.au/PictureGallery/logos/pages/CGFC%20logo_jpg.htm

Reason: Just a bit more time to make changes and the weekend for me to look at things closely and to choose. Thanks, Lumi

Thanks for all the submissions. So many of them are really works of art. Not one of them are not good. The ones that I am eliminating are the ones that I think are not suitable for me personally only, and because if I don't, it makes it very difficult to decide as many of you are also sending me slight variations of a card. I have just decided to choose a second place card too. Can't thank you all enough. Good luck, Lumi. P.S - Working today till 10 pm as the card says :-), so probably won't be able to give a feedback till late Saturday night or Sunday morning here in Sydney, Australia. 

Reason: Just added a second place to the budget and realised that Australia is ahead of the rest of the world in the time zone (only :-) - don't want to offend anyone or start a debate!! ) , so Monday deadline will mean it will be a weekend for the rest of the world. Just wanted to give everyone more time to submit their best, especially since I will be picking a second card too. Can't thank everyone enough for the submissions. P.S - Not keen on photos on the card.

Contact Information for Business Card

Dr. Lumi Harcourt M.B.B.S., F.C.G.F.C
Family General Practitioner
Address, timings, phone and fax number on the back.

Requirements
Must have
• Timings
Mon 7 am - 7 pm
Tues 7 am - 12 pm
Wed 7 am - 10 pm
Thurs 7 am - 12 pm
Fri 7 am - 8 pm
Sat 8 am - 10 pm
Sun - Off

```html
<!DOCTYPE html>
<html lang="en">
<head>
<meta charset="utf-8">
<title>Dr. Lumi Harcourt – Business Card</title>
<link rel="stylesheet" href="https://fonts.googleapis.com/css2?family=Crimson+Text:ital,wght@0,400;0,600;0,700;1,400&display=swap">
<style>
  :root {
    --page-bg: #e9e6e1;
    --navy: #1f3f6e;
    --navy-deep: #16305a;
    --band-blue: #2d5a92;
    --band-blue-dark: #234b7d;
    --paper: #f4f5f6;
    --paper-shade: #dfe2e6;
    --skin-light: #e9c2a6;
    --skin-mid: #d49c7c;
    --cloth: #f2f2f0;
    --white: #ffffff;
    --soft-white: rgba(255,255,255,0.78);
  }
  * { box-sizing: border-box; margin: 0; padding: 0; }
  html, body { width: 1200px; height: 880px; overflow: hidden; }
  body {
    background: var(--page-bg);
    font-family: "Crimson Text", Georgia, serif;
    position: relative;
  }

  .card {
    position: absolute;
    overflow: hidden;
    box-shadow: 0 6px 18px rgba(0,0,0,0.18);
  }

  /* ---------- Front ---------- */
  .card-front {
    left: 135px; top: 285px;
    width: 540px; height: 309px;
    background: linear-gradient(180deg, var(--white) 0%, var(--paper) 60%, var(--paper-shade) 100%);
  }
  .front-photo {
    position: absolute;
    left: 248px; top: 0;
    width: 292px; height: 212px;
    background:
      radial-gradient(ellipse 70% 80% at 35% 45%, var(--skin-light) 0%, var(--skin-mid) 65%, rgba(212,156,124,0) 100%),
      linear-gradient(180deg, var(--paper) 0%, var(--cloth) 100%);
  }
  .guild-mark {
    position: absolute;
    left: 50px; top: 26px;
    display: flex; align-items: center; gap: 8px;
    color: var(--navy);
    font-weight: 700;
    font-size: 26px;
    letter-spacing: 1px;
  }
  .guild-mark .dot {
    width: 22px; height: 22px;
    border-radius: 50%;
    background: var(--navy);
  }
  .tagline {
    position: absolute;
    left: 42px; top: 112px;
    color: var(--navy);
    font-weight: 700;
    font-size: 26px;
    line-height: 27px;
  }
  .tagline .second { display: block; padding-left: 30px; }

  .name-band {
    position: absolute;
    left: 0; bottom: 0;
    width: 100%; height: 102px;
    background: linear-gradient(180deg, var(--band-blue) 0%, var(--band-blue-dark) 100%);
    border-top: 3px solid rgba(255,255,255,0.55);
  }
  .name-band .rule {
    position: absolute;
    left: 32px; top: 16px;
    width: 2px; height: 56px;
    background: var(--soft-white);
  }
  .doctor-name {
    position: absolute;
    left: 44px; top: 12px;
    color: var(--white);
    font-weight: 700;
    font-size: 30px;
    line-height: 32px;
    white-space: nowrap;
  }
  .doctor-name .credentials {
    font-size: 12px;
    font-weight: 600;
    letter-spacing: 0.5px;
    margin-left: 6px;
  }
  .doctor-role {
    position: absolute;
    left: 44px; top: 46px;
    color: var(--soft-white);
    font-size: 19px;
  }

  /* ---------- Back ---------- */
  .card-back {
    left: 755px; top: 170px;
    width: 309px; height: 540px;
    background: radial-gradient(ellipse 90% 70% at 45% 40%, #2f578c 0%, var(--navy) 55%, var(--navy-deep) 100%);
    color: var(--white);
    padding: 34px 30px 0 34px;
  }
  .hours {
    width: 100%;
    border-collapse: collapse;
    font-size: 22px;
  }
  .hours td { padding: 2px 0; line-height: 28px; }
  .hours .day { font-weight: 700; }
  .hours .time { text-align: right; font-weight: 400; }

  .divider {
    height: 1px;
    background: var(--soft-white);
    margin: 20px 0 18px;
  }
  .address {
    font-style: normal;
    font-size: 17px;
    line-height: 23px;
    color: var(--soft-white);
  }
  .contact {
    width: 100%;
    border-collapse: collapse;
    font-size: 26px;
  }
  .contact td { line-height: 34px; }
  .contact .label { font-weight: 700; }
  .contact .number { text-align: right; }
</style>
</head>
<body>

  <section class="card card-front" aria-label="Business card front">
    <div class="front-photo" role="img" aria-label="Photograph of a pregnant woman's belly with her hands resting on it"></div>

    <div class="guild-mark">
      <span class="dot"></span>
      <span class="guild-name">CGFC</span>
    </div>

    <p class="tagline">Caring about<span class="second">your health!</span></p>

    <div class="name-band">
      <span class="rule"></span>
      <h1 class="doctor-name">Dr. Lumi Harcourt<span class="credentials">M.B.B.S., F.C.G.F.C.</span></h1>
      <p class="doctor-role">Family General Practitioner</p>
    </div>
  </section>

  <section class="card card-back" aria-label="Business card back">
    <table class="hours">
      <tr><td class="day">Monday</td><td class="time">7 AM - 7 PM</td></tr>
      <tr><td class="day">Tuesday</td><td class="time">7 AM - 12 PM</td></tr>
      <tr><td class="day">Wednesday</td><td class="time">7 AM - 10 PM</td></tr>
      <tr><td class="day">Thursday</td><td class="time">7 AM - 12 PM</td></tr>
      <tr><td class="day">Friday</td><td class="time">7 AM - 8 PM</td></tr>
      <tr><td class="day">Saturday</td><td class="time">8 AM - 10 PM</td></tr>
      <tr><td class="day">Sunday</td><td class="time">Off</td></tr>
    </table>

    <div class="divider"></div>

    <address class="address">
      Upper Level, Harbour Walk,<br>
      Lindale Grove Shopping Centre<br>
      Lindale Hill, NSW 2999
    </address>

    <div class="divider"></div>

    <table class="contact">
      <tr><td class="label">Phone</td><td class="number">02 5550 1400</td></tr>
      <tr><td class="label">Fax</td><td class="number">02 55501433</td></tr>
    </table>
  </section>

</body>
</html>
```